Business Card Design

I am a new realtor. To stand out from the other 25 realtors in my firm I need a card that will stand out. I am the youngest realtor here, so I want something to reflect that. Something different, as opposed to the same old traditional, boring cards everyone else has. It of course needs to have my picture which I will download for you ( I included a black and white option as well as color. Either are fine) and you can crop it or do whatever you need to make it look the best. Our company colors are red and white. These don't have to be the only colors on the card, but the red especially needs to be a focal color. I like a clean, stream-line look while still eye-catching. Not over the top busy.
While I do have to provide the company logo, I am a contractor. Therefore, I want the focus on me and my information.
Industry/Entity Type
Realtor
Contact Information for Business Card
Marisa Quillon
Realtor (this needs the realtor logo which has the R in the circle at the end)
(office)555.318.4406
(cell) 555.892.6035
Mquillon@brv-homegroup.example
It will also need our company logo which I will download and send
Requirements
Nice to have
- I like the look of the foil or metallic. However, this is definitely not a requirement

```html
<!DOCTYPE html>
<html lang="en">
<head>
<meta charset="utf-8">
<title>Business Card – Marisa Quillon</title>
<link rel="stylesheet" href="https://fonts.googleapis.com/css2?family=Tinos:wght@700&family=Open+Sans:wght@400&display=swap">
<style>
  :root {
    --brand-red: #d81a1b;
    --band-black: #0b0b0b;
    --paper-white: #ffffff;
    --backdrop: #ece9e4;
    --photo-hair: #7a4a34;
    --photo-skin: #d9b19a;
    --photo-blouse: #f1eeec;
  }
  * { box-sizing: border-box; margin: 0; padding: 0; }
  html, body {
    width: 1200px; height: 1178px; overflow: hidden;
    background: var(--backdrop);
  }
  .canvas { position: relative; width: 1200px; height: 1178px; }

  .card {
    position: absolute;
    box-shadow: 0 2px 6px rgba(0,0,0,.18);
    overflow: hidden;
  }
  .card--front { left: 29px; top: 35px; width: 908px; height: 519px; background: var(--brand-red); }
  .card--back  { left: 260px; top: 611px; width: 905px; height: 517px; background: var(--paper-white); border: 1px solid #bbb; }

  .company-frame {
    position: absolute; left: 26px; top: 34px; width: 438px; height: 212px;
    border: 2px solid var(--paper-white);
    display: flex; align-items: center; justify-content: center;
  }

  .company-name {
    font-family: "Open Sans", sans-serif;
    font-weight: 400;
    text-align: center;
    line-height: 1.3;
  }
  .company-name span { display: block; }
  .card--front .company-name { color: var(--paper-white); font-size: 34px; }
  .card--front .company-name .tagline { font-size: 26px; margin-top: 6px; }

  .card--back .company-name {
    position: absolute; left: 0; top: 0; width: 100%; height: 100%;
    display: flex; flex-direction: column; justify-content: center;
    color: var(--brand-red); font-size: 50px; line-height: 1.35;
  }
  .card--back .company-name .tagline { font-size: 38px; margin-top: 10px; }

  .name-band {
    position: absolute; left: 0; top: 291px; width: 665px; height: 55px;
    background: var(--band-black);
  }
  .name-band::before, .name-band::after {
    content: ""; position: absolute; left: 0; width: 100%; height: 2px; background: var(--paper-white);
  }
  .name-band::before { top: -7px; }
  .name-band::after { bottom: -7px; }
  .agent-name {
    position: absolute; left: 60px; top: 11px;
    font-family: "Tinos", serif; font-weight: 700; font-size: 27px;
    color: var(--paper-white); white-space: nowrap;
  }

  .contact-list { position: absolute; left: 55px; top: 368px; list-style: none; }
  .contact-item {
    display: flex; align-items: center; height: 46px;
    font-family: "Open Sans", sans-serif; font-size: 25px; color: var(--paper-white);
  }
  .contact-icon { width: 24px; height: 24px; margin-right: 8px; flex: none; }

  .agent-photo {
    position: absolute; left: 573px; top: 101px; width: 335px; height: 418px;
    background: linear-gradient(180deg, var(--photo-hair) 0%, var(--photo-skin) 30%, var(--photo-hair) 55%, var(--photo-blouse) 75%, var(--photo-blouse) 100%);
  }
</style>
</head>
<body>
<main class="canvas">
  <section class="card card--front">
    <div class="company-frame">
      <div class="company-name">
        <span>Harriet Vale</span>
        <span>&amp; Company</span>
        <span class="tagline">Real Estate Brokerage</span>
      </div>
    </div>

    <div class="name-band"><span class="agent-name">Marisa Quillon®</span></div>

    <ul class="contact-list">
      <li class="contact-item">
        <svg class="contact-icon" viewBox="0 0 24 24" fill="none" stroke="#fff" stroke-width="2"><circle cx="12" cy="12" r="10"/><path d="M8 7c0 5 4 9 9 10l1-3-3-1-1 1c-2-1-3-2-4-4l1-1-1-3z" fill="#fff" stroke="none"/></svg>
        555.318.4406
      </li>
      <li class="contact-item">
        <svg class="contact-icon" viewBox="0 0 24 24"><rect x="6" y="3" width="12" height="19" rx="2" fill="#fff"/><rect x="8" y="6" width="8" height="6" fill="#d81a1b"/><rect x="8" y="14" width="8" height="6" fill="#d81a1b" opacity=".35"/></svg>
        555.892.6035
      </li>
      <li class="contact-item">
        <svg class="contact-icon" viewBox="0 0 24 24"><path d="M2 10l10-6 10 6v10H2z" fill="#fff"/><path d="M2 10l10 6 10-6" fill="none" stroke="#d81a1b" stroke-width="1.5"/></svg>
        Mquillon@brv-homegroup.example
      </li>
    </ul>

    <div class="agent-photo" role="img" aria-label="Portrait photo of the realtor in a white blouse"></div>
  </section>

  <section class="card card--back">
    <div class="company-name">
      <span>Harriet Vale</span>
      <span>&amp; Company</span>
      <span class="tagline">Real Estate Brokerage</span>
    </div>
  </section>
</main>
</body>
</html>
```